Pop up exhibition stand 2000mm (H) x 800mm (W)

I would like a simple pop up banner stand for an exhibition.

We need a pop up banner stand design for 'Brindle Forge Services'

the size is 2000mm(H) x 800mm (W)

Ad copy as follows :

[Brindle Forge logo]

From Sheet Metal To Large Sand Castings

Our Capacity and Rapid Quenching drop bottom ovens deliver precise processing.
We also serve the leading names in aerospace, automotive and advanced engineering.

Visit www.brindleforge-example.co.uk/ or call us Tel: +44 (0)1632 960418

[Put the crafted in the shires logo here, also include the text member somewhere close]

check on their website for other ideas that can help you with this project.

Target Market(s)

will be used at a trade show

Requirements
Nice to have
• modern design for UK manufacturing business

```html
<!DOCTYPE html>
<html lang="en">
<head>
<meta charset="utf-8">
<title>Brindle Forge Services – Exhibition Banner</title>
<link rel="stylesheet" href="https://fonts.googleapis.com/css2?family=Barlow:wght@400;500;600;700&display=swap">
<style>
  :root {
    --brand-red: #e3232c;
    --ink-grey: #8d9296;
    --ink-dark: #5a6065;
    --paper: #ffffff;
  }
  * { margin: 0; padding: 0; box-sizing: border-box; }
  html, body { width: 1200px; height: 3000px; overflow: hidden; background: var(--paper); }
  .banner {
    position: relative;
    width: 1200px;
    height: 3000px;
    overflow: hidden;
    background: var(--paper);
    font-family: "Barlow", "Arial", sans-serif;
  }
  .banner__photos { position: absolute; inset: 0; }

  .brand {
    position: absolute;
    top: 52px;
    right: 40px;
    display: flex;
    align-items: center;
    gap: 22px;
  }
  .brand__name {
    display: flex;
    align-items: center;
    gap: 14px;
    font-size: 62px;
    font-weight: 700;
    color: var(--brand-red);
    line-height: 1;
  }
  .brand__mark { width: 36px; height: 36px; background: var(--brand-red); }
  .brand__tagline {
    font-size: 27px;
    font-weight: 500;
    color: var(--brand-red);
    line-height: 1.15;
  }

  .headline-panel {
    position: absolute;
    left: 0; top: 720px;
    width: 928px; height: 600px;
    background: var(--paper);
    padding: 46px 0 0 98px;
  }
  .headline {
    font-size: 126px;
    font-weight: 700;
    line-height: 1.02;
    color: var(--brand-red);
    text-transform: uppercase;
    letter-spacing: 2px;
  }

  .info-panel {
    position: absolute;
    left: 0; top: 1380px;
    width: 928px; height: 590px;
    background: var(--paper);
    padding: 66px 0 0 94px;
    color: var(--ink-grey);
    font-size: 34px;
    line-height: 1.5;
  }
  .info-panel p { margin-bottom: 44px; max-width: 780px; }
  .info-panel .contact { font-weight: 600; color: var(--ink-dark); }

  .origin-badge {
    position: absolute;
    left: 94px; top: 1862px;
    display: flex;
    align-items: center;
    gap: 16px;
  }
  .origin-badge__mark {
    width: 92px; height: 92px;
    border-radius: 50%;
    border: 7px solid var(--brand-red);
    flex: none;
  }
  .origin-badge__name {
    font-size: 30px;
    font-weight: 700;
    line-height: 1.05;
    color: var(--brand-red);
    text-transform: uppercase;
  }
  .origin-badge__member {
    display: block;
    margin-top: 6px;
    font-size: 24px;
    font-weight: 500;
    color: var(--ink-dark);
    text-transform: lowercase;
  }
</style>
</head>
<body>
<main class="banner">

  <svg class="banner__photos" width="1200" height="3000" viewBox="0 0 1200 3000">
    <defs>
      <linearGradient id="hall" x1="0" y1="0" x2="1" y2="1">
        <stop offset="0" stop-color="#7b7f80"/>
        <stop offset="0.35" stop-color="#c9c7bf"/>
        <stop offset="0.6" stop-color="#e2e1dc"/>
        <stop offset="1" stop-color="#a9a8a2"/>
      </linearGradient>
      <linearGradient id="portrait" x1="0" y1="0" x2="0" y2="1">
        <stop offset="0" stop-color="#4f5559"/>
        <stop offset="0.45" stop-color="#c79f8d"/>
        <stop offset="0.8" stop-color="#f1f1f1"/>
        <stop offset="1" stop-color="#d9dadb"/>
      </linearGradient>
      <linearGradient id="engineer" x1="0" y1="0" x2="1" y2="1">
        <stop offset="0" stop-color="#3f4448"/>
        <stop offset="0.3" stop-color="#b79584"/>
        <stop offset="0.55" stop-color="#eceeef"/>
        <stop offset="0.75" stop-color="#9e2a2e"/>
        <stop offset="1" stop-color="#e9ebec"/>
      </linearGradient>
      <linearGradient id="rail" x1="0" y1="0" x2="1" y2="0">
        <stop offset="0" stop-color="#6a7074"/>
        <stop offset="0.5" stop-color="#c8c6bd"/>
        <stop offset="1" stop-color="#8a8d8c"/>
      </linearGradient>
      <linearGradient id="furnace" x1="0" y1="0" x2="1" y2="1">
        <stop offset="0" stop-color="#3c97d6"/>
        <stop offset="0.55" stop-color="#1f6ea9"/>
        <stop offset="1" stop-color="#22343f"/>
      </linearGradient>
      <linearGradient id="floor" x1="0" y1="0" x2="1" y2="1">
        <stop offset="0" stop-color="#d8d7cf"/>
        <stop offset="0.45" stop-color="#8b8d8a"/>
        <stop offset="0.7" stop-color="#c9a48f"/>
        <stop offset="1" stop-color="#5e6366"/>
      </linearGradient>
      <linearGradient id="blocks" x1="0" y1="0" x2="1" y2="1">
        <stop offset="0" stop-color="#d6d8da"/>
        <stop offset="0.4" stop-color="#9fa5aa"/>
        <stop offset="0.7" stop-color="#e7e9ea"/>
        <stop offset="1" stop-color="#7f868c"/>
      </linearGradient>
    </defs>

    <polygon role="img" aria-label="Photo: factory hall with heat treatment ovens and overhead gantry"
      points="0,250 1200,220 1200,1980 0,1980" fill="url(#hall)"/>
    <polygon role="img" aria-label="Photo: portrait of a company director in white shirt and red tie"
      points="0,250 380,245 380,720 0,720" fill="url(#portrait)"/>
    <polygon role="img" aria-label="Photo: engineer in white shirt and red tie inspecting a large casting"
      points="928,560 1200,470 1200,1980 928,1980" fill="url(#engineer)"/>
    <rect role="img" aria-label="Photo: workshop rail and machinery detail"
      x="0" y="1320" width="928" height="60" fill="url(#rail)"/>
    <polygon role="img" aria-label="Photo: blue industrial furnace structure"
      points="0,1980 560,1980 0,2560" fill="url(#furnace)"/>
    <polygon role="img" aria-label="Photo: workshop floor with a large metal ring casting held by hand"
      points="620,1980 1200,1980 1200,2250 0,2960 0,2620" fill="url(#floor)"/>
    <polygon role="img" aria-label="Photo: machined aluminium blocks on a rack"
      points="1200,2320 1200,3000 40,3000" fill="url(#blocks)"/>

    <polygon points="380,720 1200,205 1200,265 470,720" fill="#ffffff"/>
    <polygon points="560,1980 620,1980 0,2620 0,2560" fill="#ffffff"/>
    <polygon points="1200,2250 1200,2320 40,3000 -40,3000" fill="#ffffff"/>
  </svg>

  <header class="brand">
    <div class="brand__name"><span class="brand__mark"></span>Brindle Forge</div>
    <p class="brand__tagline">the solution in<br>aluminium heat treatment</p>
  </header>

  <section class="headline-panel">
    <h1 class="headline">From Sheet<br>Metal to<br>Large Sand<br>Castings</h1>
  </section>

  <section class="info-panel">
    <p>Our Capacity and Rapid Quenching drop bottom ovens deliver precise processing.</p>
    <p>We also serve the leading names in aerospace, automotive and advanced engineering.</p>
    <p class="contact">Visit www.brindleforge-example.co.uk/<br>or call us Tel: +44 (0)1632 960418</p>
  </section>

  <div class="origin-badge">
    <span class="origin-badge__mark"></span>
    <p class="origin-badge__name">Crafted in<br>the shires<span class="origin-badge__member">member</span></p>
  </div>

</main>
</body>
</html>
```